We need our website look and feel updated to match our brand

We are looking to update our website and a "where to buy" tab at the top of the website. The current look and feel is ok but needs a clean up. The task is as follows:
1. Update the current pages and add a page for "Where to Buy"
2. Update the product page to reflect our current products. ie we have only three products now. Undercoat K, Undercoat M and GLAZEX. This page will have very similar descriptions and at the bottom of each product will be a link to our SDS (safety data sheets).
3. Please visit our current website for the look and feel.
4. Use our New Taglines need to be included. "Always Cleaning. All the Time." "24/7 SAFE SURFACE PROTECTION" (Logo as well)
5. The HomePage will need a nice clean location to our corporate video. https://clipvue.net/8kRtWmPzQaL (link for viewing) that will be the highlight and easy to access on the homepage.
Some examples of websites we like.
https://velmarix.com/
https://quorbelhall.com/ (like the use of motion graphics in these)
Our focus claims are that our product is a surface cleaner and deodorizer. We would like to see variations in black, white background (Black header bar) and Gray backgrounds.

```html
<!DOCTYPE html>
<html lang="en">
<head>
<meta charset="utf-8">
<title>Lumacoat – 24/7 Safe Surface Protection</title>
<link href="https://fonts.googleapis.com/css2?family=Poppins:wght@400;500;600;700&display=swap" rel="stylesheet">
<style>
:root{
  --black:#000;
  --ink:#0d0d0d;
  --panel:#1f1f1f;
  --yellow:#f9c10b;
  --white:#fff;
  --muted:#d8d8d8;
}
*{box-sizing:border-box;margin:0;padding:0}
html,body{width:1200px;height:4124px;overflow:hidden;background:var(--black);font-family:'Poppins',sans-serif;color:var(--white)}
.page{position:relative;width:1200px;height:4124px}
.abs{position:absolute}
.brand{display:flex;align-items:center;gap:10px}
.brand-mark{width:22px;height:22px;background:var(--yellow)}
.brand-name{font-weight:600;font-size:40px;color:var(--white);letter-spacing:-.5px}
.yl{color:var(--yellow)}
/* header */
.header{left:0;top:0;width:1200px;height:150px;background:var(--black)}
.contact-box{top:37px;height:74px;background:#2b2b2b;border-radius:4px;display:flex;align-items:center;padding:0 16px;gap:14px}
.contact-box small{display:block;font-size:12px;font-weight:600}
.contact-box strong{display:block;font-size:19px;font-weight:600}
.nav{left:0;top:150px;width:1200px;height:56px;background:var(--yellow);display:flex;align-items:center;padding-left:180px}
.nav a{color:var(--black);font-size:14px;font-weight:500;text-decoration:none;padding:0 15px;height:56px;line-height:56px}
.nav a.active{background:var(--black);color:var(--yellow)}
/* hero */
.hero{left:0;top:206px;width:1200px;height:594px;background:linear-gradient(160deg,#6a6a6a,#3a3a3a 55%,#2a2a2a)}
.hero-box{left:248px;top:164px;width:710px;height:183px;background:rgba(20,20,20,.7);text-align:center;padding-top:30px}
.hero-box h1{font-size:38px;font-weight:700;line-height:50px}
.btn{display:inline-block;background:var(--yellow);color:var(--black);font-weight:600;font-size:14px;padding:10px 19px}
.arrow{width:44px;height:44px;border-radius:50%;background:rgba(255,255,255,.35);top:275px}
.dots{left:568px;top:518px;display:flex;gap:6px}
.dots i{width:12px;height:12px;border-radius:50%;background:var(--white)}
.dots i:first-child{background:var(--yellow)}
/* sections */
.title{width:1200px;left:0;text-align:center;font-size:38px;font-weight:700;letter-spacing:.5px}
.product{top:950px;width:316px;height:442px;background:radial-gradient(circle at 50% 55%,#f4f0e0,#8a8a82 70%,#1a1a1a)}
.product.featured{border:4px solid var(--yellow)}
.product.k{background:radial-gradient(ellipse at 50% 55%,#f5f5f2,#b8b8b0 55%,#111 80%)}
.product.m{background:radial-gradient(ellipse at 50% 55%,#f2c366,#c98c2a 50%,#111 80%)}
.product.g{background:radial-gradient(ellipse at 50% 55%,#f8ea6a,#d9c23a 50%,#111 80%)}
.product span{position:absolute;left:50%;bottom:90px;transform:translateX(-50%);background:#111;color:var(--white);font-weight:600;font-size:17px;padding:8px 14px}
.framed{left:0;width:1200px;border:4px solid var(--yellow);background:linear-gradient(120deg,#1a1a1a,#2a2a2a 60%,#151515)}
.p{font-size:14px;line-height:21.5px;color:var(--white);text-align:justify}
.h2{font-size:38px;font-weight:700}
.video{left:632px;top:2177px;width:456px;height:273px;background:linear-gradient(135deg,#8fd0f0,#f4f4f4 60%,#f0b83c)}
.play{right:12px;top:12px;width:50px;height:50px;border-radius:50%;background:var(--yellow);display:flex;align-items:center;justify-content:center}
.feature{width:260px;text-align:center;font-size:14px;line-height:21px}
.feature .ring{width:126px;height:126px;border-radius:50%;background:var(--yellow);border:4px solid var(--black);outline:3px solid var(--yellow);margin:0 auto 16px;display:flex;align-items:center;justify-content:center}
.tile{width:478px;height:266px;display:flex;align-items:center;justify-content:center}
.tile span{background:var(--yellow);color:var(--white);font-weight:600;font-size:16px;padding:8px 14px}
/* footer */
.footer h4{font-size:21px;font-weight:600;margin-bottom:18px}
.footer li{list-style:none;font-size:14px;line-height:30px;display:flex;align-items:center;gap:12px}
.footer li::before{content:"";width:9px;height:9px;border:2px solid var(--yellow);border-radius:50%}
.social{display:flex;gap:8px}
.social i{width:24px;height:24px;border-radius:50%}
</style>
</head>
<body>
<div class="page">

<header class="header abs">
  <div class="abs brand" style="left:110px;top:42px"><span class="brand-mark"></span><span class="brand-name">Lumacoat</span></div>
  <div class="abs contact-box" style="left:478px;width:335px">
    <svg width="44" height="44" viewBox="0 0 44 44" fill="none" stroke="#f9c10b" stroke-width="2"><rect x="5" y="12" width="34" height="24"/><path d="M5 12l17 14 17-14"/></svg>
    <div><small>Mail us Today :</small><strong>info@companyname.com</strong></div>
  </div>
  <div class="abs contact-box" style="left:825px;width:263px">
    <svg width="44" height="44" viewBox="0 0 44 44" fill="none" stroke="#f9c10b" stroke-width="2"><circle cx="22" cy="22" r="19"/><path d="M15 13l5 5-3 3c2 4 4 6 8 8l3-3 5 5-3 3c-8 0-18-10-18-18z"/></svg>
    <div><small>Call us Today :</small><strong>+1 888 888 8888</strong></div>
  </div>
</header>

<nav class="nav abs">
  <a class="active">HOME</a><a>ABOUT US</a><a>PRODUCTS</a><a>WHERE TO BUY</a><a>OUR TECHNOLOGY</a><a>NEWS</a><a>FAQ</a><a>CONTACT</a>
</nav>

<section class="hero abs" role="img" aria-label="Close-up of a periodic table showing titanium and neighbouring elements">
  <div class="abs arrow" style="left:70px"></div>
  <div class="abs arrow" style="left:1086px"></div>
  <div class="abs hero-box">
    <h1>Always Cleaning. All the Time.<br>24/7 SAFE SURFACE PROTECTION</h1>
    <span class="btn" style="margin-top:14px;font-size:13px">GET STARTED</span>
  </div>
  <div class="abs dots"><i></i><i></i><i></i><i></i></div>
</section>

<h2 class="abs title" style="top:872px"><span class="yl">LUMACOAT</span> PRODUCTS</h2>
<div class="abs product k" style="left:110px" role="img" aria-label="Gallon jug of Undercoat K"><span>UNDERCOAT K</span></div>
<div class="abs product m featured" style="left:442px" role="img" aria-label="Gallon jug of Undercoat M"><span>UNDERCOAT M</span></div>
<div class="abs product g" style="left:773px" role="img" aria-label="Gallon jug of Glazex"><span>GLAZEX</span></div>

<section class="abs framed" style="top:1483px;height:558px">
  <div class="abs" style="left:71px;top:33px;width:520px;height:490px;background:var(--white);padding:9px">
    <div style="width:100%;height:100%;background:linear-gradient(135deg,#c37a3a,#7a4a2a 50%,#3a3a3a)" role="img" aria-label="Business handshake"></div>
  </div>
  <div class="abs" style="left:628px;top:62px;width:492px">
    <div class="h2"><span class="yl">REAL WORLD</span> SOLUTION</div>
    <p class="p" style="margin-top:14px">The onset of COVID-19 has changed our lives forever. The current methods of cleaning surfaces are not sustainable. Cleaning the environment we live in with caustic UV-C light, ammonia-based cleaners and other harsh chemicals is wasteful. The moment you clean the surface and an infected person touches that surface again, it requires reapplication of your protective cleaners.</p>
    <p class="p" style="margin-top:21px">Lumacoat is bringing a permanent surface coating formula to the United States market. A titanium dioxide photocatalyst coating that is incredibly long lasting and durable. How long? It basically lasts as long as the substrate is present. As long as it's not mechanically removed or painted over, Lumacoat lasts for decades on any surface, indoor or outdoor.</p>
    <span class="btn" style="margin-top:22px;font-size:13px;padding:11px 24px">READ MORE</span>
  </div>
</section>

<h2 class="abs title" style="top:2098px"><span class="yl">HOW IT</span> WORKS</h2>
<div class="abs" style="left:110px;top:2170px;width:490px">
  <p class="p">The onset of COVID-19 has changed our lives forever. The current methods of cleaning surfaces are not sustainable. Cleaning the environment, we live in with caustic UV-C light, ammonia-based cleaners and other harsh chemicals is wasteful. The moment you clean the surface and an infected person touches that surface again it requires reapplication of whatever you are using to keep the surfaces clean and safe.</p>
  <p class="p" style="margin-top:21px">Not with Lumacoat!</p>
  <p class="p" style="margin-top:21px">Lumacoat is bringing a permanent surface coating formula to the United States market. A titanium dioxide photocatalyst coating that is incredibly long lasting and durable.</p>
</div>
<div class="abs video" role="img" aria-label="Corporate video preview: illustrated worker spraying surface coating">
  <div class="abs play"><svg width="20" height="20" viewBox="0 0 20 20"><path d="M5 2l13 8-13 8z" fill="#000"/></svg></div>
</div>
<div class="abs feature" style="left:145px;top:2515px">
  <div class="ring"><svg width="60" height="60" viewBox="0 0 60 60" fill="none" stroke="#000" stroke-width="2"><rect x="16" y="14" width="28" height="32" rx="3"/><path d="M22 24h16M22 31h16M22 38h10"/></svg></div>
  How long? It basically lasts as long as the substrate is present. As long as it's not mechanically removed, Lumacoat lasts for decades on any surface, indoor or outdoor.
</div>
<div class="abs feature" style="left:470px;top:2575px">
  <div class="ring"><svg width="60" height="60" viewBox="0 0 60 60" fill="none" stroke="#000" stroke-width="2"><path d="M12 44l12-16 8 8 6-6 10 14z"/><path d="M30 16l2 4 4 1-4 1-2 4-2-4-4-1 4-1z"/></svg></div>
  <div style="text-align:justify">How durable? The coating is optically clear and as hard as toughened glass. Activated by light the coating constantly decomposes organic particles like dirt and microorganisms in real-time, using</div>only water vapor and oxygen.
</div>
<div class="abs feature" style="left:795px;top:2515px">
  <div class="ring"><svg width="60" height="60" viewBox="0 0 60 60" fill="none" stroke="#000" stroke-width="2"><path d="M16 42l26-26M20 46l26-26"/><circle cx="40" cy="20" r="6"/></svg></div>
  Please note, as of March 2021, Lumacoat has not been approved or validated by the United States EPA regulations. Lumacoat is beginning the process of EPA certification.
</div>

<section class="abs framed" style="top:2950px;height:783px;background:linear-gradient(180deg,#111,#262626 60%,#151515)">
  <h2 class="abs title" style="top:76px;left:-4px"><span class="yl">LUMACOAT</span> PROJECTS</h2>
  <div class="abs tile" style="left:106px;top:140px;background:linear-gradient(135deg,#bfe6f8,#3a8fd0)" role="img" aria-label="Hospital operating room"><span>UNIVERSITY HOSPITAL</span></div>
  <div class="abs tile" style="left:606px;top:140px;background:linear-gradient(135deg,#8a99aa,#c9a24a 55%,#c8201e)" role="img" aria-label="Fast food restaurant storefront"><span>BURGERTON VOLCANO</span></div>
  <div class="abs tile" style="left:106px;top:422px;background:linear-gradient(135deg,#d8dee6,#4d7ab8 60%,#2a4a80)" role="img" aria-label="Public bathroom stalls"><span>ODORLESS BATHROOMS</span></div>
  <div class="abs tile" style="left:606px;top:422px;background:linear-gradient(135deg,#8a2020,#3a3a3a 55%,#cfcfcf)" role="img" aria-label="Toll booth with coated and non coated sections"><span>TOLL BOOTH TEST</span></div>
</section>

<footer class="abs footer" style="left:0;top:3733px;width:1200px;height:391px">
  <div class="abs brand" style="left:110px;top:96px"><span class="brand-mark"></span><span class="brand-name">Lumacoat</span></div>
  <div class="abs" style="left:110px;top:150px;font-size:16px;letter-spacing:2px">CERTIFIED INSTALLER</div>
  <p class="abs p" style="left:110px;top:190px;width:228px;font-size:14px;line-height:21px">Our US company was formed to take advantage of 20 years of experience with Titanium Dioxide in Japan. Our team is focused on real world solutions that are useful</p>
  <div class="abs" style="left:445px;top:87px"><h4>Quick Links</h4><ul><li>Home</li><li>About Us</li><li>FAQ'S</li><li>Contact Us</li></ul></div>
  <div class="abs" style="left:660px;top:87px"><h4>Useful Links</h4><ul><li>Our Products</li><li>Our Technology</li><li>News</li></ul></div>
  <div class="abs" style="left:857px;top:87px"><h4>Contact us</h4><ul><li>Phone : +1 888 888 8888</li><li>Email: contactus@lumacoat.net</li><li>Location: Brookvale, CT USA</li></ul></div>
  <div class="abs" style="left:420px;top:274px;width:668px;height:1px;background:#555"></div>
  <div class="abs social" style="left:445px;top:295px"><i style="background:#3b5998"></i><i style="background:#1da1f2"></i><i style="background:#dd4b39"></i><i style="background:#cb2027"></i></div>
  <div class="abs" style="left:836px;top:297px;font-size:13px">© Company name. All rights reserved.</div>
</footer>

</div>
</body>
</html>
```